Redo my diagrams for print in a Magazine - files attached - ASAP

Hi, I have 3 diagrams that I have done that are dodgy, that I need to look good. They need to be high quality to be printed in a magazine for an article I am writing. And of course I need them yesterday. Actually I need them in 8 hours.

If there was a A4 version that could be downloaded, that would be excellent.

Cheers

Rob

Target Market(s)

Medial Magazine article

Industry/Entity Type

Medical

Font styles to use
Sans Serif

Requirements
Must have
• Must be able to be printed, in a magazine.
Nice to have
• Nice to have an A4 downloadable version

```html
<!DOCTYPE html>
<html lang="en">
<head>
<meta charset="utf-8">
<title>Findings on MRI in people without pain</title>
<link rel="stylesheet" href="https://fonts.googleapis.com/css2?family=Montserrat:wght@400;700;800&display=swap">
<style>
:root{
  --ink:#111;
  --paper:#fff;
  --red:#d7193a;
  --magenta:#a3237f;
  --purple:#4b2a82;
  --blue:#1f5fa3;
  --cyan:#1ab3e6;
  --orange:#ee8a1e;
  --yellow:#f6d21a;
  --green:#8bbf3c;
  --deep-green:#1c6b3a;
  --hip-box:#c55a9b;
  --knee-box:#f7de12;
  --back-box:#1ab2e4;
}
*{box-sizing:border-box;margin:0;padding:0}
html,body{width:1200px;height:2553px;overflow:hidden;background:var(--paper)}
body{font-family:"Montserrat",Arial,sans-serif;color:var(--ink);position:relative}
.guides{position:absolute;left:0;top:0}
.abs{position:absolute}
.section-title{font-size:36px;font-weight:800;line-height:1.12;letter-spacing:-.5px;white-space:nowrap}
.stat .value{font-size:32px;font-weight:800;line-height:1}
.stat .label{font-size:17px;line-height:1.2;margin-top:4px;white-space:nowrap}
.stat.right{text-align:right}
.inline-value{font-size:32px;font-weight:800}
.scan{position:absolute;border-radius:50%}
.scan-hip{background:radial-gradient(circle at 45% 45%,#9a9a9a 0%,#5e5e5e 45%,#262626 100%)}
.scan-knee{background:radial-gradient(circle at 50% 45%,#8e8e8e 0%,#4a4a4a 50%,#141414 100%)}
.scan-back{background:radial-gradient(circle at 55% 50%,#8a8a8a 0%,#444 50%,#121212 100%)}
.pain-box{position:absolute;padding:20px 22px;line-height:1.15}
.pain-box .big{font-size:28px;font-weight:800;white-space:nowrap}
.pain-box .big span{font-size:22px}
.pain-box p{font-size:18px;margin-top:4px;white-space:nowrap}
.box-hip{background:var(--hip-box);color:#fff}
.box-knee{background:var(--knee-box)}
.box-back{background:var(--back-box)}
.box-hip .big,.box-back .big{color:var(--ink)}
.citation{font-size:11.5px;line-height:1.35;color:#222}
.divider{position:absolute;left:0;width:1200px;height:4px;background:var(--ink)}
.note{font-size:16px;text-align:right;line-height:1.25;white-space:nowrap}
.question{font-size:22px;font-weight:800;line-height:1.12;text-align:right;white-space:nowrap}
.age-table{position:absolute;left:442px;top:2272px;width:280px;border-collapse:collapse;font-size:13px}
.age-table th{background:var(--ink);color:#fff;font-weight:800;font-size:17px;padding:0 8px;height:30px}
.age-table th .ends{display:flex;justify-content:space-between;align-items:center}
.age-table td{padding:0 6px;height:23px;border-bottom:1px solid #999}
.age-table td.pct{font-weight:800;width:46px}
.age-table td.pct.end{text-align:right}
.age-table td.name{text-align:center;white-space:nowrap}
</style>
</head>
<body>

<svg class="guides" width="1200" height="2553" viewBox="0 0 1200 2553" aria-hidden="true">
  <defs>
    <g id="ring" fill="none" stroke-width="14">
      <circle r="200" stroke="var(--red)" pathLength="360" stroke-dasharray="78 360" stroke-dashoffset="-280" transform="rotate(-90)"/>
      <circle r="200" stroke="var(--magenta)" pathLength="360" stroke-dasharray="58 360" transform="rotate(-90)"/>
      <circle r="200" stroke="var(--purple)" pathLength="360" stroke-dasharray="28 360" stroke-dashoffset="-60" transform="rotate(-90)"/>
      <circle r="200" stroke="var(--blue)" pathLength="360" stroke-dasharray="38 360" stroke-dashoffset="-90" transform="rotate(-90)"/>
      <circle r="200" stroke="var(--cyan)" pathLength="360" stroke-dasharray="30 360" stroke-dashoffset="-130" transform="rotate(-90)"/>
      <circle r="200" stroke="var(--orange)" pathLength="360" stroke-dasharray="38 360" stroke-dashoffset="-240" transform="rotate(-90)"/>
      <circle r="200" stroke="var(--yellow)" pathLength="360" stroke-dasharray="43 360" stroke-dashoffset="-195" transform="rotate(-90)"/>
    </g>
  </defs>

  <!-- hip -->
  <use href="#ring" transform="translate(609 411) scale(1.2)"/>
  <g transform="translate(609 411) scale(1.2)" fill="none" stroke-width="14">
    <circle r="200" stroke="var(--green)" pathLength="360" stroke-dasharray="21 360" stroke-dashoffset="-172" transform="rotate(-90)"/>
    <circle r="200" stroke="var(--deep-green)" pathLength="360" stroke-dasharray="5 360" stroke-dashoffset="-166" transform="rotate(-90)"/>
  </g>
  <g stroke="var(--ink)" stroke-width="1.5" stroke-dasharray="7 4 2 4" fill="none">
    <path d="M108 270 V281 H395"/>
    <path d="M108 377 V388 H363"/>
    <path d="M108 557 V568 H421"/>
    <path d="M108 642 V653 H497"/>
    <path d="M108 737 V748 H566 V658"/>
    <path d="M1092 240 V262 H806"/>
    <path d="M1092 360 V382 H852"/>
    <path d="M1092 445 V496 H840"/>
    <path d="M1092 556 V607 H754"/>
  </g>
  <g fill="var(--ink)">
    <circle cx="1092" cy="240" r="5"/><circle cx="1092" cy="360" r="5"/>
    <circle cx="1092" cy="445" r="5"/><circle cx="1092" cy="556" r="5"/>
  </g>

  <!-- knee -->
  <use href="#ring" transform="translate(614 1210) scale(1.025)"/>
  <g stroke="var(--ink)" stroke-width="1.5" stroke-dasharray="7 4 2 4" fill="none">
    <path d="M108 1122 V1133 H417"/>
    <path d="M108 1217 V1228 H403"/>
    <path d="M108 1345 V1323 H436"/>
    <path d="M1092 1041 V1092 H789"/>
    <path d="M1092 1135 V1184 H824"/>
    <path d="M1092 1233 V1282 H813"/>
    <path d="M1092 1336 V1384 H729"/>
  </g>
  <path d="M1112 1336 V1532 H1092" fill="none" stroke="var(--cyan)" stroke-width="2"/>
  <circle cx="1112" cy="1336" r="5" fill="var(--cyan)"/>
  <g fill="var(--ink)">
    <circle cx="1092" cy="1041" r="5"/><circle cx="1092" cy="1135" r="5"/>
    <circle cx="1092" cy="1233" r="5"/><circle cx="1092" cy="1336" r="5"/>
  </g>

  <!-- back -->
  <use href="#ring" transform="translate(629 2045)"/>
  <g stroke="var(--ink)" stroke-width="1.5" stroke-dasharray="7 4 2 4" fill="none">
    <path d="M108 1979 V1990 H430"/>
    <path d="M108 2079 V2090 H427"/>
    <path d="M108 2172 V2183 H477"/>
    <path d="M1092 1910 V1958 H816"/>
    <path d="M1092 1996 V2044 H836"/>
    <path d="M1092 2099 V2146 H809"/>
    <path d="M1092 2185 V2255 H660"/>
    <path d="M400 2287 H442"/>
  </g>
  <g fill="var(--ink)">
    <circle cx="1092" cy="1910" r="5"/><circle cx="1092" cy="1996" r="5"/>
    <circle cx="1092" cy="2099" r="5"/><circle cx="1092" cy="2185" r="5"/>
    <circle cx="400" cy="2287" r="5"/>
  </g>
</svg>

<!-- ============ HIP ============ -->
<section class="panel panel-hip">
  <h2 class="section-title abs" style="left:106px;top:62px">What people with no pain,<br>have on their hip MRI’s</h2>
  <div class="scan scan-hip" style="left:387px;top:189px;width:444px;height:444px" role="img" aria-label="Coronal MRI scan of a hip joint"></div>

  <div class="stat abs" style="left:116px;top:219px"><div class="value">73%</div><div class="label">have some sort of abnormality</div></div>
  <div class="stat abs" style="left:116px;top:326px"><div class="value">69%</div><div class="label">have labral tears</div></div>
  <div class="stat abs" style="left:116px;top:506px"><div class="value">24%</div><div class="label">have cartilage defects</div></div>
  <div class="stat abs" style="left:116px;top:591px"><div class="value">11% have</div><div class="label">have bone oedema</div></div>
  <div class="stat abs" style="left:116px;top:686px"><div class="value">2.2%</div><div class="label">have ligamentum teres tears</div></div>

  <div class="stat right abs" style="right:120px;top:219px"><div class="label">CAM lesions are seens in <span class="inline-value">20%</span></div></div>
  <div class="stat right abs" style="right:120px;top:310px"><div class="label">Labral and parabral cysts<br>are seen in <span class="inline-value">13%</span></div></div>
  <div class="stat right abs" style="right:120px;top:429px"><div class="value">16%</div><div class="label">have subchondral cysts</div></div>
  <div class="stat right abs" style="right:120px;top:540px"><div class="value">11%</div><div class="label">have rim fractures</div></div>

  <div class="pain-box box-hip" style="left:754px;top:630px;width:292px;height:150px">
    <div class="big">0% <span>have pain</span></div>
    <p>Just because<br>it is on the scan<br>doesn’t mean it hurts</p>
  </div>

  <p class="citation abs" style="left:146px;top:797px;width:940px">Harlow K, Ventris D, Okafor L, Lindqvist M, Abrey P, Morel T. Prevalence of abnormal hip findings in asymptomatic participants : a prospective, blinded study. Clin Sports Rev. 2012 Dec;40(12):2720-4.</p>
</section>

<div class="divider" style="top:852px"></div>

<!-- ============ KNEE ============ -->
<section class="panel panel-knee">
  <h2 class="section-title abs" style="left:106px;top:909px">What people with no pain,<br>have on their knee MRI’s</h2>
  <div class="scan scan-knee" style="left:425px;top:1021px;width:378px;height:378px" role="img" aria-label="Sagittal MRI scan of a knee joint"></div>

  <div class="stat abs" style="left:116px;top:1071px"><div class="value">88%</div><div class="label">have at least one abnormality (1)</div></div>
  <div class="stat abs" style="left:116px;top:1166px"><div class="value">72%</div><div class="label">have osteophytes(1)</div></div>
  <div class="stat abs" style="left:116px;top:1340px"><div class="label">Bone marrow lesions are seen in</div><div class="value">51% <span style="font-size:14px;font-weight:400">(1)</span></div></div>

  <div class="pain-box box-knee" style="left:158px;top:1420px;width:284px;height:150px">
    <div class="big">0% <span>have pain</span></div>
    <p>Just because<br>it is on the scan<br>doesn’t mean it hurts</p>
  </div>

  <div class="stat right abs" style="right:120px;top:1025px"><div class="value">68%</div><div class="label">have cartilage damage (1)</div></div>
  <div class="stat right abs" style="right:120px;top:1119px"><div class="value">36%</div><div class="label">have synovitis (1)</div></div>
  <div class="stat right abs" style="right:120px;top:1217px"><div class="value">9%</div><div class="label">Have torn ligaments (1)</div></div>
  <div class="stat right abs" style="right:120px;top:1320px"><div class="value">25%</div><div class="label">have meniscal tears (1)</div></div>

  <p class="note abs" style="right:120px;top:1398px">But in people over 50,<br><b>60%</b> of peope with <b>NO PAIN</b><br>have meniscal tears(1)</p>
  <p class="note abs" style="right:120px;top:1480px">and only <b>63%</b> people <b>WITH PAIN</b><br>have meniscal tears (2)</p>

  <p class="citation abs" style="left:146px;top:1611px;width:940px">1. Castellan R, Obi N, Varga S, Holm E, Tessier J, Amaro P, et al. Prevalence of abnormalities in knees detected by MRI in adults without knee osteoarthritis: population based observational study (Larkfield Joint Cohort). Northgate Medical Press. 2012; 345:e5339.<br>2. Holm E, Castellan R, Pryce D, Navarro J, Sato K, Whelan F, et al. Incidental meniscal findings on knee MRI in middle-aged and elderly persons. J Clin Musculoskel. 2008 Sep 11;359(11):1108-15.</p>
</section>

<div class="divider" style="top:1702px"></div>

<!-- ============ BACK ============ -->
<section class="panel panel-back">
  <h2 class="section-title abs" style="left:106px;top:1765px">What people with no pain,<br>have on their back MRI’s</h2>
  <div class="scan scan-back" style="left:445px;top:1861px;width:368px;height:368px" role="img" aria-label="Sagittal MRI scan of a lumbar spine"></div>

  <div class="stat abs" style="left:116px;top:1903px"><div class="value">83%</div><div class="label">have a disc bulge, protrusion<br>or extrusion (1)</div></div>
  <div class="stat abs" style="left:116px;top:2028px"><div class="value">37%</div><div class="label">have facet joint arthritis (3)</div></div>
  <div class="stat abs" style="left:116px;top:2121px"><div class="value">33%</div><div class="label">have high intensity zones (1)</div></div>

  <div class="stat right abs" style="right:120px;top:1894px"><div class="value">22%</div><div class="label">have discs contacting nerves (1)</div></div>
  <div class="stat right abs" style="right:120px;top:1980px"><div class="value">23%</div><div class="label">have annular fissures (3)</div></div>
  <div class="stat right abs" style="right:120px;top:2083px"><div class="value">73%</div><div class="label">have disc degeneration (1)(2)(3)</div></div>
  <div class="stat right abs" style="right:120px;top:2169px"><div class="value">17%</div><div class="label">have a disc pushing<br>on the Thecal sac (1)</div></div>

  <p class="question abs" style="right:826px;top:2272px">What’s the<br>difference between<br>20 and 80 year olds<br>no back pain? (4)</p>

  <table class="age-table">
    <thead><tr><th colspan="3"><div class="ends"><span>20</span><span>AGE</span><span>80</span></div></th></tr></thead>
    <tbody>
      <tr><td class="pct">37%</td><td class="name">Disc degeneration</td><td class="pct end">96%</td></tr>
      <tr><td class="pct">17%</td><td class="name">Disc signal loss</td><td class="pct end">97%</td></tr>
      <tr><td class="pct">24%</td><td class="name">Disc height loss</td><td class="pct end">84%</td></tr>
      <tr><td class="pct">30%</td><td class="name">Disc bulge</td><td class="pct end">84%</td></tr>
      <tr><td class="pct">29%</td><td class="name">Disc protrusion</td><td class="pct end">43%</td></tr>
      <tr><td class="pct">19%</td><td class="name">Annular fissure</td><td class="pct end">29%</td></tr>
      <tr><td class="pct">4%</td><td class="name">Facet degeneration</td><td class="pct end">83%</td></tr>
      <tr><td class="pct">3%</td><td class="name">Spondylolisthesis</td><td class="pct end">50%</td></tr>
    </tbody>
  </table>

  <div class="pain-box box-back" style="left:802px;top:2292px;width:284px;height:160px">
    <div class="big">0% <span>have pain</span></div>
    <p>Just because<br>it is on the scan<br>doesn’t mean it hurts</p>
  </div>

  <p class="citation abs" style="left:100px;top:2494px;width:1060px;font-size:10px;line-height:1.3">1. Brenner U, Falk O, Idris H, Moss G. MR imaging of the lumbar spine: prevalence of intervertebral disk extrusion and sequestration, nerve root compression, end plate abnormalities, and osteoarthritis of the facet joints in asymptomatic volunteers. Imaging Rev. 1998;209(3):661-6<br>2. Park JW, Seo HN, Cho DY. Prevalence of disc degeneration in asymptomatic subjects. Part 1 : lumbar spine. Asian Spine Rep. 2013 Jan;53(1):31-8.<br>3. Ashdown V, et al. Systematic literature review of imaging features of spinal degeneration in asymptomatic populations. Neuroimaging Q. 2015 Apr;36(4):811-6</p>
</section>

</body>
</html>
```